My Book needs a front and back cover design

I need you to design my front and back cover of my book. The title of my book is : Beyond the Silent Pause
My Story
5 steps to speaking fluently forever

The picture that I uploaded needs to be on the front cover. On the back cover it should be excerpt from Chapter One like this :

As years have gone by I have become much more conscious about my problem with stuttering, more able to relax my muscles to alleviate it. At the age of 20, I realized that stuttering is like a demon in my head that needs to be killed and that nothing is wrong with me. Furthermore, no one can help me but myself. I'm holding the key of my future. Everything is just in my head.

With this book, I want to help you realize that nobody can help you fix your stuttering better than yourself. There's no quick-get-rid-of-stuttering cure. The cure lies inside of you.

- Lukas Orbeck, excerpt from Chapter One
----------------------------------------------------------------------------------

My name also needs to be located on the front cover.

Target Market(s)

80 million people who stutter each day

Industry/Entity Type

Psychology

Font styles to use
Serif
Sans Serif

Colors
1b1b1b
000000
333333

Requirements
Must have
• Front Cover : Full Title and subtitle and my name and my picture
• Back Cover : Excerpt from my Chapter One with my name below just as I have described in my project description
Nice to have
• Maybe black background would be the best for the front cover.

```html
<!DOCTYPE html>
<html lang="en">
<head>
<meta charset="utf-8">
<title>Beyond the Silent Pause — Cover Spread</title>
<link rel="stylesheet" href="https://fonts.googleapis.com/css2?family=Tinos:wght@400;700&family=Arimo:wght@700&display=swap">
<style>
  :root {
    --stage: #9a9a9a;
    --cover: #000000;
    --cover-soft: #1b1b1b;
    --cover-mid: #333333;
    --ink: #ffffff;
    --accent: #2ec9c9;
    --serif: "Tinos", "Times New Roman", serif;
    --sans: "Arimo", Arial, sans-serif;
  }
  html, body {
    margin: 0;
    padding: 0;
    width: 1200px;
    height: 1200px;
    overflow: hidden;
    background: var(--stage);
  }
  .spread {
    position: relative;
    width: 1200px;
    height: 1200px;
  }
  .cover {
    position: absolute;
    top: 280px;
    width: 432px;
    height: 617px;
    background: var(--cover);
    color: var(--ink);
    overflow: hidden;
  }
  .cover--back { left: 162px; }
  .cover--front { left: 626px; }

  /* Back cover */
  .excerpt {
    position: absolute;
    left: 62px;
    top: 105px;
    width: 310px;
    font-family: var(--serif);
    font-weight: 700;
    font-size: 11.2px;
    line-height: 18px;
    margin: 0;
  }
  .excerpt p { margin: 0 0 18px; }
  .author-photo {
    position: absolute;
    left: 60px;
    top: 414px;
    width: 101px;
    height: 109px;
    border: 1px solid var(--accent);
    background: radial-gradient(ellipse at 50% 40%, #4a3a32 0%, #1b1b1b 45%, #0a0a0a 100%);
  }
  .author-credit {
    position: absolute;
    left: 62px;
    top: 534px;
    font-family: var(--serif);
    font-weight: 700;
    font-size: 11.2px;
    line-height: 18px;
    margin: 0;
  }

  /* Front cover */
  .hero-photo {
    position: absolute;
    inset: 0;
    background:
      radial-gradient(ellipse 30% 22% at 52% 22%, #8a6a58 0%, rgba(60,45,38,0.6) 55%, transparent 100%),
      radial-gradient(ellipse 50% 55% at 52% 75%, #141414 0%, #0c0c0c 70%, transparent 100%),
      linear-gradient(180deg, #1b1b1b 0%, #111 60%, #050505 100%);
  }
  .title {
    position: absolute;
    left: 72px;
    top: 276px;
    margin: 0;
    font-family: var(--serif);
    font-weight: 400;
    color: var(--ink);
    line-height: 1;
  }
  .title__lead {
    display: block;
    font-size: 29px;
  }
  .title__main {
    display: block;
    font-size: 54px;
    margin-top: 4px;
  }
  .subtitle-block {
    position: absolute;
    left: 72px;
    top: 502px;
    font-family: var(--sans);
    font-weight: 700;
    color: var(--ink);
  }
  .subtitle-block__story { font-size: 22px; line-height: 26px; margin: 0; }
  .subtitle-block__steps { font-size: 15px; line-height: 20px; margin: 0; }
  .subtitle-block__author { font-size: 11px; line-height: 17px; margin: 0; }
</style>
</head>
<body>
<main class="spread">
  <section class="cover cover--back" aria-label="Back cover">
    <div class="excerpt">
      <p>Excerpt from Chapter One like this :</p>
      <p>As years have gone by I have become much more conscious about my problem with stuttering, more able to relax my muscles to alleviate it. At the age of 20, I realized that stuttering is like a demon in my head that needs to be killed and that nothing is wrong with me. Furthermore, no one can help me but myself. I’m holding the key of my future. Everything is just in my head.</p>
      <p>With this book, I want to help you realize that nobody can help you fix your stuttering better than yourself. There’s no quick-get-rid-of-stuttering cure. The cure lies inside of you.</p>
    </div>
    <div class="author-photo" role="img" aria-label="Small portrait photo of the author in a dark shirt against a black background"></div>
    <p class="author-credit">- Lukas Orbeck,<br>excerpt from Chapter One</p>
  </section>

  <section class="cover cover--front" aria-label="Front cover">
    <div class="hero-photo" role="img" aria-label="Full-cover portrait photo of the author standing in a black polo shirt against a dark background"></div>
    <h1 class="title">
      <span class="title__lead">Beyond the</span>
      <span class="title__main">Silent Pause</span>
    </h1>
    <div class="subtitle-block">
      <p class="subtitle-block__story">My Story</p>
      <p class="subtitle-block__steps">5 steps to speaking fluently forever</p>
      <p class="subtitle-block__author">- Lukas Orbeck</p>
    </div>
  </section>
</main>
</body>
</html>
```